Business card for consulting firm

We need a double-sided business card for consulting firm, VantoriX. The card should be professional but also creative and visually interesting.

Target Market(s)

Engineering and technology; transport industries; safety critical / heavy industry.

Contact Information for Business Card

See attached file with details.

Font styles to use
Sans Serif

```html
<!DOCTYPE html>
<html lang="en">
<head>
<meta charset="utf-8">
<title>VantoriX – Business Card</title>
<link href="https://fonts.googleapis.com/css2?family=Work+Sans:wght@400;500;600&display=swap" rel="stylesheet">
<style>
  :root {
    --navy: #0d2238;
    --navy-deep: #0a1a2b;
    --cyan: #1fb3e6;
    --white: #ffffff;
    --paper: #f4f5f6;
    --logo-grey: #d4d7da;
    --ink: #4a4f55;
    --ink-navy: #1e2f5e;
    --backdrop: #e7e9ec;
  }
  * { margin: 0; padding: 0; box-sizing: border-box; }
  html, body {
    width: 1200px; height: 900px; overflow: hidden;
    background: var(--backdrop);
    font-family: "Work Sans", sans-serif;
  }
  .canvas { position: relative; width: 1200px; height: 900px; }
  .card {
    position: absolute; left: 250px;
    width: 700px; height: 400px;
    border-radius: 22px; overflow: hidden;
    box-shadow: 0 10px 30px rgba(10, 26, 43, 0.25);
    background: radial-gradient(ellipse at 40% 30%, var(--navy), var(--navy-deep));
  }
  .card--back { top: 30px; }
  .card--front { top: 470px; }
  .wordmark {
    position: absolute;
    color: var(--logo-grey);
    font-weight: 500;
    letter-spacing: 0.08em;
    text-transform: uppercase;
  }
  .card--back .wordmark {
    left: 0; right: 0; top: 160px;
    text-align: center; font-size: 64px;
  }
  .card--front .wordmark { left: 48px; top: 44px; font-size: 40px; }
  .card-shape { position: absolute; inset: 0; }
  .details {
    position: absolute; right: 36px; top: 168px;
    text-align: right;
  }
  .name {
    color: var(--cyan); font-size: 29px; font-weight: 500;
    text-transform: uppercase; letter-spacing: 0.01em;
  }
  .credentials { color: var(--ink-navy); font-size: 13px; font-weight: 500; margin-top: 2px; }
  .role { color: var(--ink-navy); font-size: 17px; margin-top: 4px; padding-right: 30px; }
  .contact-list { list-style: none; margin-top: 16px; }
  .contact-list li {
    display: flex; justify-content: flex-end; align-items: center; gap: 12px;
    color: var(--ink); font-size: 18px; line-height: 27px;
  }
  .contact-list svg { width: 16px; height: 16px; flex: none; }
</style>
</head>
<body>
<main class="canvas">
  <section class="card card--back" aria-label="Card back">
    <div class="wordmark">VantoriX</div>
  </section>

  <section class="card card--front" aria-label="Card front">
    <svg class="card-shape" viewBox="0 0 700 400" width="700" height="400" aria-hidden="true">
      <path d="M0,400 L0,372 Q280,120 700,142 L700,400 Z" fill="var(--paper)"/>
      <path d="M0,372 Q280,120 700,142" fill="none" stroke="var(--cyan)" stroke-width="7"/>
    </svg>
    <div class="wordmark">VantoriX</div>
    <div class="details">
      <h1 class="name">Morgan Ellery</h1>
      <p class="credentials">BA (Hons), M Psych Org, M Tech Mgt (HF)</p>
      <p class="role">Managing Director</p>
      <ul class="contact-list">
        <li>+61 (0)400 555 017
          <svg viewBox="0 0 16 16"><path d="M4 1.5l2.5 3-1.5 1.6a8 8 0 0 0 4.9 4.9l1.6-1.5 3 2.5-1.6 2.2C7.5 14 2 8.5 1.8 3.1z" fill="var(--cyan)"/></svg>
        </li>
        <li>mellery@vantorix.com.au
          <svg viewBox="0 0 16 16"><rect x="1.5" y="3.5" width="13" height="9" rx="1" fill="none" stroke="var(--cyan)" stroke-width="1.5"/><path d="M2 4l6 5 6-5" fill="none" stroke="var(--cyan)" stroke-width="1.5"/></svg>
        </li>
        <li>www.vantorix.global
          <svg viewBox="0 0 16 16"><circle cx="8" cy="8" r="6.5" fill="none" stroke="var(--cyan)" stroke-width="1.4"/><ellipse cx="8" cy="8" rx="3" ry="6.5" fill="none" stroke="var(--cyan)" stroke-width="1.2"/><path d="M1.5 8h13" stroke="var(--cyan)" stroke-width="1.2"/></svg>
        </li>
        <li>www.vantorix.com.au
          <svg viewBox="0 0 16 16"><circle cx="8" cy="8" r="6.5" fill="none" stroke="var(--cyan)" stroke-width="1.4"/><ellipse cx="8" cy="8" rx="3" ry="6.5" fill="none" stroke="var(--cyan)" stroke-width="1.2"/><path d="M1.5 8h13" stroke="var(--cyan)" stroke-width="1.2"/></svg>
        </li>
      </ul>
    </div>
  </section>
</main>
</body>
</html>
```